Lumindo Business Card

Need a business card for our business.

Attached are our Logos. There is either the white and black all the all red with white. Either Logo can be used.

The winner will be provided the details for phone number and address.

Good Luck!

Business

```html
<!DOCTYPE html>
<html lang="en">
<head>
<meta charset="utf-8">
<title>Lumindo Industries Business Card</title>
<link rel="stylesheet" href="https://fonts.googleapis.com/css2?family=Open+Sans:wght@400;600;700;800&display=swap">
<style>
  :root {
    --backdrop: #2b2b2b;
    --card-red-light: #9a1a20;
    --card-red-dark: #5c0b0f;
    --card-white: #f1f0ee;
    --brand-red: #b3171d;
    --silver: #d9d9d9;
    --ink: #3a3a3a;
  }
  * { margin: 0; padding: 0; box-sizing: border-box; }
  html, body {
    width: 1200px;
    height: 716px;
    overflow: hidden;
    background: var(--backdrop);
    font-family: "Open Sans", Arial, sans-serif;
  }
  .stage {
    position: relative;
    width: 1200px;
    height: 716px;
    display: flex;
    align-items: center;
    justify-content: center;
    gap: 60px;
  }
  .card {
    position: relative;
    width: 520px;
    height: 298px;
    border-radius: 3px;
    box-shadow: 0 10px 30px rgba(0,0,0,0.45);
  }
  .card--front {
    background: radial-gradient(ellipse at 40% 40%, var(--card-red-light), var(--card-red-dark));
    display: flex;
    flex-direction: column;
    align-items: center;
    justify-content: center;
  }
  .wordmark {
    font-weight: 800;
    text-transform: uppercase;
    text-align: center;
    line-height: 1;
  }
  .card--front .wordmark { color: var(--silver); }
  .wordmark__name {
    display: block;
    font-size: 74px;
    letter-spacing: -1px;
  }
  .wordmark__sub {
    display: block;
    font-size: 26px;
    letter-spacing: 22px;
    margin-top: 10px;
    padding-left: 22px;
  }
  .card--back { background: var(--card-white); }
  .card--back .wordmark {
    position: absolute;
    left: 34px;
    top: 96px;
    color: var(--brand-red);
  }
  .card--back .wordmark__name { font-size: 42px; }
  .card--back .wordmark__sub {
    font-size: 15px;
    letter-spacing: 12px;
    margin-top: 6px;
    padding-left: 12px;
  }
  .holder {
    position: absolute;
    left: 340px;
    top: 92px;
  }
  .holder__name {
    color: var(--brand-red);
    font-size: 13px;
    font-weight: 700;
    text-transform: uppercase;
    letter-spacing: 0.5px;
  }
  .holder__role {
    color: var(--ink);
    font-size: 9px;
    font-weight: 600;
  }
  .contact {
    position: absolute;
    left: 340px;
    top: 180px;
    font-size: 10px;
    line-height: 1.5;
    color: var(--ink);
    font-style: normal;
  }
  .contact__line { display: block; }
  .contact__address { margin-bottom: 5px; }
  .contact__web {
    color: var(--brand-red);
    font-weight: 600;
    margin-top: 6px;
  }
</style>
</head>
<body>
  <main class="stage">
    <section class="card card--front" aria-label="Card front">
      <div class="wordmark">
        <span class="wordmark__name">Lumindo</span>
        <span class="wordmark__sub">Industries</span>
      </div>
    </section>

    <section class="card card--back" aria-label="Card back">
      <div class="wordmark">
        <span class="wordmark__name">Lumindo</span>
        <span class="wordmark__sub">Industries</span>
      </div>
      <div class="holder">
        <p class="holder__name">Mara Ellison</p>
        <p class="holder__role">Director</p>
      </div>
      <address class="contact">
        <span class="contact__line contact__address">Your Address, Building<br>City, Country XXXXX</span>
        <span class="contact__line">Tel: XXX XXX XXXX</span>
        <span class="contact__line">Fax: XXX XXX XXXX</span>
        <span class="contact__line contact__web">www.lumindoworks.com</span>
      </address>
    </section>
  </main>
</body>
</html>
```